Designs for a fundrasining event a Brown Tie Beer and Wine event

We need a flyer, brochure, and tickets for entry for a brown tie event that will be a beer and wine pairing fundraising event to be held on May 9th from 6pm to 10pm at the Maplecrest Restaurant in Cedar Lake, Indiana, USA. There will be approximately 10 silent auction items and 5 or so sponsors that we will want to have the logos of the sponsors on what we can as well, attached are the logo for Open Hearth Foundation, IV NFP, which is the nonprofit hosting the event, there is also a logo for Dunmore Law, LLC which is one of the sponsors (this is so you have an idea of the other 4 or so that we would also want incorporated somehow). Please ask as many questions as you may have to clarify.

Industry/Entity Type

Event

Contact Information for Business Card

Open Hearth
Wendy P. Halvorsen
President/CEO
(555)384-9062
www.openhearthfdn.example.org

New Card:
Marcus J. Halvorsen
Director
(555)627-3148
www.openhearthfdn.example.org

New Card:
Norma T. Halvorsen
Director
www.openhearthfdn.example.org

New Card:
Gerald K. Halvorsen
Director
www.openhearthfdn.example.org

Font styles to use
Script

Requirements
Must have
• I want a clean card for all 4 individuals with the logo that was attached.

```html
<!DOCTYPE html>
<html lang="en">
<head>
<meta charset="utf-8">
<title>Wine and Beer Pairing – Admission Ticket</title>
<link rel="stylesheet" href="https://fonts.googleapis.com/css2?family=Great+Vibes&family=Tenor+Sans&display=swap">
<style>
  :root {
    --bg-dark: #2b1613;
    --bg-mid: #4a3431;
    --bg-light: #9a9391;
    --ink-light: #ffffff;
    --title-ink: #dccfcc;
    --ornament: #e6e4cf;
    --badge-fill: #ecebdc;
    --badge-ink: #a33a2a;
    --beer-gold: #d8a23c;
    --beer-foam: #efe6cf;
    --wine-red: #5e0d12;
  }
  html, body {
    margin: 0;
    padding: 0;
    width: 1200px;
    height: 686px;
    overflow: hidden;
  }
  .ticket {
    position: relative;
    width: 1200px;
    height: 686px;
    overflow: hidden;
    background: linear-gradient(90deg, var(--bg-dark) 0%, var(--bg-mid) 45%, var(--bg-light) 100%);
    font-family: "Tenor Sans", sans-serif;
    color: var(--ink-light);
  }
  .ornament {
    position: absolute;
    top: 70px;
    height: 32px;
    border-radius: 16px 16px 4px 4px;
    background: var(--ornament);
    opacity: 0.85;
  }
  .ornament--left { left: 86px; width: 308px; }
  .ornament--right { left: 732px; width: 298px; }
  .admit-one {
    position: absolute;
    top: 64px;
    left: 394px;
    width: 338px;
    text-align: center;
    font-size: 34px;
    letter-spacing: 1px;
  }
  .event-title {
    position: absolute;
    top: 112px;
    left: 60px;
    width: 980px;
    margin: 0;
    text-align: center;
    font-family: "Great Vibes", cursive;
    font-weight: 400;
    font-size: 104px;
    line-height: 1;
    color: var(--title-ink);
    text-shadow: 3px 4px 6px rgba(0,0,0,0.55);
    white-space: nowrap;
  }
  .details {
    position: absolute;
    top: 258px;
    left: 316px;
    width: 660px;
    text-align: center;
  }
  .details p {
    margin: 0;
    font-size: 50px;
    line-height: 67px;
  }
  .details .venue {
    font-variant: small-caps;
    font-size: 42px;
    letter-spacing: 1px;
  }
  .auction-badge {
    position: absolute;
    left: 22px;
    top: 286px;
    width: 322px;
    height: 196px;
    border-radius: 50%;
    background: var(--badge-fill);
    box-shadow: 4px 6px 10px rgba(0,0,0,0.5);
    display: flex;
    align-items: center;
    justify-content: center;
    text-align: center;
    font-family: "Great Vibes", cursive;
    font-size: 52px;
    line-height: 50px;
    color: var(--badge-ink);
  }
  .drinks-photo {
    position: absolute;
    right: 0;
    top: 0;
    width: 194px;
    height: 686px;
    background:
      linear-gradient(180deg, transparent 0%, transparent 3%, var(--wine-red) 10%, var(--wine-red) 28%, transparent 36%),
      linear-gradient(180deg, transparent 0%, transparent 36%, var(--beer-foam) 38%, var(--beer-gold) 48%, #b9802a 80%, #d9c8a8 100%);
    border-left: 2px solid rgba(255,255,255,0.25);
  }
</style>
</head>
<body>
  <main class="ticket">
    <div class="ornament ornament--left" role="img" aria-label="Decorative scroll flourish"></div>
    <div class="admit-one">ADMIT ONE</div>
    <div class="ornament ornament--right" role="img" aria-label="Decorative scroll flourish"></div>

    <h1 class="event-title">Wine and Beer Pairing</h1>

    <div class="auction-badge"><span>Plus<br>Silent<br>auction</span></div>

    <section class="details">
      <p>Saturday, May 9, 2015</p>
      <p>6 pm to10 pm</p>
      <p class="venue">Maplecrest Restaurant</p>
      <p>4820 Harborview Ave.</p>
      <p>Cedar Lake, IN</p>
    </section>

    <div class="drinks-photo" role="img" aria-label="Photo of a glass of red wine above a glass of foamy beer"></div>
  </main>
</body>
</html>
```